■依頼目的/概要
電子書籍を出版しますので、
表紙デザイン作成をお願いいたします。

■本のタイトル
ソラトビ!
~港町発 17才女子高生社長の留学奮闘記~

<著者>株式会社七海舎 代表取締役社長 柴田遥香
※参考に株式会社七海舎 の社名ロゴを添付します。

■本の内容

「株式会社七海舎」の代表取締役社長である
著者、柴田遥香さんが、
海外で感じた事や、

高校生でありながら起業に至る経緯などを、
JKらしい軽快な文体で本にしました。

※参考に本の原稿を資料として添付します。

高校2年生の海外渡航体験で、
東南アジアのエネルギーを
目の当たりにしたことをきっかけに、

「日本の元気のなさってヤバくない?」
「もっと10代のうちに海外を見ようよ!」
と、心の底から感じました。

その思いを形にすべく、現在は、
10代向け海外留学支援サイト「ソラトビ!」を、
立ち上げ運営しています。サイトはこちらです。

https://soratobi-site.example/profile/
※ソラトビ!ロゴを参考材料として添付します。

■デザイン要望

16才の遥香社長の元気でチャレンジャーな感じを表現したいです。

できれば、
遥香さんの写真を使いたいと思っています。

※遥香さんの写真を材料として添付します。
※株式会社七海舎の会社ロゴ、
および運営サイト「ソラトビ!」のロゴも参考に添付しますので、
使用についてはデザイナーさんにお任せします。

その他の
イラストや写真等素材を使用される場合には、
商用利用可の素材をお願いします。

色合い、デザインレイアウトとも、
デザイナーさんにお任せしたいと思います。

■その他、デザインを考えるのに必要な情報などありましたら、
お答えしますので、遠慮なく聞いて下さい。

※添付資料
・遥香社長の写真
・株式会社七海舎のロゴ画像
・留学サイト「ソラトビ!」のロゴ
・原稿たたき
素晴らしいご提案をいただきありがとうございます。
提案予約のご連絡をいただきましたため、
締切日時を2日だけ延長させていただきます。

引き続き、よろしくお願いいたします。

かなり悩みましたが、
ぱっとみてわかりやすい、
ロゴにインパクトがあった、
パブリックな感じがポイントになりました。

この度はご提案いただきありがとうございました。
たくさんのいい提案があり、選考に本当に迷いました。
ご応募してくださったワーカーのみなさまに感謝いたします。

また依頼することもあるかと思いますので、
その時はよろしくお願いいたします。

```html
<!DOCTYPE html>
<html lang="ja">
<head>
<meta charset="utf-8">
<title>ソラトビ! 表紙</title>
<link rel="stylesheet" href="https://fonts.googleapis.com/css2?family=M+PLUS+Rounded+1c:wght@800;900&family=Noto+Sans+JP:wght@500;700;900&display=swap">
<style>
  :root {
    --sky-top: #2f9fe0;
    --sky-mid: #7cc3ee;
    --ground: #4a5a3e;
    --navy: #17306e;
    --blue-text: #1d4fa8;
    --white: #ffffff;
    --pink: #ff4f9a;
    --yellow: #ffd21f;
    --cyan: #2aa8ff;
    --green: #3ec84a;
    --red: #f2342b;
    --ink: #1a1a1a;
  }
  * { margin: 0; padding: 0; box-sizing: border-box; }
  html, body { width: 752px; height: 1200px; overflow: hidden; background: #fff; }
  .cover {
    position: relative;
    width: 752px; height: 1200px;
    overflow: hidden;
    font-family: "Noto Sans JP", sans-serif;
  }
  .cover-photo {
    position: absolute; inset: 0;
    background: linear-gradient(180deg, #5d4a3a 0%, #7a6552 18%, var(--sky-top) 26%, var(--sky-mid) 55%, #8b9a8a 78%, var(--ground) 100%);
  }
  .title {
    position: absolute; left: 0; top: 30px; width: 752px;
    font-family: "M PLUS Rounded 1c", sans-serif;
    font-weight: 900;
    line-height: 1;
    text-align: center;
  }
  .title-line { display: block; font-size: 215px; letter-spacing: 10px; }
  .title-line + .title-line { margin-top: 40px; }
  .title span {
    -webkit-text-stroke: 6px var(--white);
    paint-order: stroke fill;
    text-shadow: 0 4px 8px rgba(0,0,0,.25);
  }
  .c-pink { color: var(--pink); }
  .c-yellow { color: var(--yellow); }
  .c-cyan { color: var(--cyan); }
  .c-green { color: var(--green); }
  .c-red { color: var(--red); }
  .catch {
    position: absolute; right: 28px; top: 608px;
    background: var(--white);
    color: var(--blue-text);
    font-weight: 700; font-size: 24px; line-height: 1.45;
    padding: 12px 18px;
    border-radius: 6px;
  }
  .subtitle {
    position: absolute; left: 0; top: 820px;
    transform: rotate(-6deg);
    transform-origin: left top;
  }
  .band {
    display: inline-block;
    background: var(--navy);
    color: var(--white);
    font-weight: 900;
    padding: 4px 20px;
    line-height: 1.15;
  }
  .band-origin { font-size: 50px; margin-left: 40px; }
  .band-main { display: block; width: max-content; font-size: 66px; margin-top: -4px; padding-left: 50px; }
  .band-main .accent { color: var(--yellow); }
  .band-tail { font-size: 66px; margin-left: 170px; margin-top: -4px; }
  .byline {
    position: absolute; left: 30px; bottom: 36px;
    display: flex; align-items: flex-end; gap: 22px;
  }
  .brand {
    display: flex; align-items: center; gap: 10px;
    color: var(--pink); font-weight: 900; font-size: 40px;
  }
  .brand-dot { width: 34px; height: 34px; border-radius: 50%; background: var(--pink); }
  .author-role {
    color: var(--ink); font-weight: 700; font-size: 26px; line-height: 1.35;
    background: rgba(255,255,255,.85); padding: 4px 10px;
  }
  .author-name {
    position: absolute; right: 30px; bottom: 36px;
    background: var(--white); color: var(--ink);
    font-weight: 900; font-size: 50px; padding: 4px 16px; letter-spacing: 4px;
  }
</style>
</head>
<body>
<main class="cover">
  <div class="cover-photo" role="img" aria-label="青空と木造の門を背景に、制服姿の女子高生が笑顔で空を指差している写真"></div>

  <h1 class="title">
    <span class="title-line"><span class="c-pink">ソ</span><span class="c-yellow">ラ</span><span class="c-cyan">ト</span></span>
    <span class="title-line"><span class="c-yellow">ビ</span><span class="c-red">!</span></span>
  </h1>

  <p class="catch">日本の元気のなさって<br>ヤバくない?<br>もっと10代のうちに<br>海外を見ようよ</p>

  <h2 class="subtitle">
    <span class="band band-origin">港町発</span>
    <span class="band band-main"><span class="accent">17才女子高生</span>社長の</span>
    <span class="band band-tail">留学奮闘記</span>
  </h2>

  <div class="byline">
    <div class="brand"><span class="brand-dot"></span>七海舎</div>
    <p class="author-role">株式会社七海舎<br>代表取締役社長</p>
  </div>
  <p class="author-name">柴田遥香</p>
</main>
</body>
</html>
```